Software engineering company needs business card

I need a cool business card. Company: Soft Belan Brindlewood Ave 41 58207 Sincity Name: Gerald Vanholt CEO / Managing Director & Owner

```html
<!DOCTYPE html>
<html lang="en">
<head>
<meta charset="utf-8">
<title>Soft Belan – Business Card</title>
<link rel="stylesheet" href="https://fonts.googleapis.com/css2?family=Open+Sans:wght@300;400;600&display=swap">
<style>
  :root {
    --page: #2b2b2b;
    --card: #333333;
    --band: #2a2a2a;
    --green: #7ab532;
    --text-light: #d6d6d6;
    --text-mid: #a8a8a8;
    --text-dim: #8c8c8c;
  }
  * { box-sizing: border-box; margin: 0; padding: 0; }
  html, body { width: 1200px; height: 1200px; overflow: hidden; }
  body {
    background: var(--page);
    font-family: "Open Sans", Arial, sans-serif;
    position: relative;
  }
  .card {
    position: absolute;
    left: 170px;
    width: 860px;
    height: 480px;
    background: var(--card);
    box-shadow: 0 6px 18px rgba(0,0,0,0.45);
    overflow: hidden;
  }
  .card--front { top: 95px; }
  .card--back { top: 625px; }

  /* Front */
  .wordmark {
    position: absolute;
    left: 0; right: 0;
    text-align: center;
    font-weight: 400;
    letter-spacing: 0.18em;
    text-transform: uppercase;
  }
  .card--front .wordmark {
    top: 78px;
    font-size: 46px;
    color: var(--text-mid);
  }
  .name-band {
    position: absolute;
    left: 0; right: 0;
    top: 180px;
    height: 100px;
    background: var(--band);
  }
  .name-band::before,
  .name-band::after {
    content: "";
    position: absolute;
    width: 5px;
    background: var(--green);
  }
  .name-band::before { left: 0; bottom: 0; height: 55px; }
  .name-band::after { right: 0; top: 0; height: 55px; }
  .holder {
    position: absolute;
    left: 0; right: 0;
    top: 204px;
    text-align: center;
  }
  .holder__name {
    font-size: 22px;
    font-weight: 400;
    color: var(--text-light);
    letter-spacing: 0.02em;
    text-transform: uppercase;
  }
  .holder__role {
    margin-top: 2px;
    font-size: 13px;
    color: var(--green);
    letter-spacing: 0.4em;
    text-transform: uppercase;
  }
  .divider {
    position: absolute;
    left: 470px;
    top: 268px;
    width: 1px;
    height: 150px;
    background: var(--green);
  }
  .contact {
    position: absolute;
    text-align: center;
    color: var(--text-light);
  }
  .contact--left { left: 60px; width: 380px; top: 312px; }
  .contact--right { left: 500px; width: 330px; top: 290px; }
  .contact__item { margin-bottom: 18px; }
  .contact__icon { display: block; margin: 0 auto 6px; }
  .contact__text { font-size: 18px; }
  .contact__text--light { font-weight: 300; color: var(--text-mid); font-size: 19px; }
  .contact__text--bold { font-weight: 600; }

  /* Back */
  .card--back .wordmark {
    top: 170px;
    font-size: 64px;
    color: var(--green);
  }
  .services {
    position: absolute;
    left: 200px;
    top: 308px;
    display: flex;
    align-items: center;
    gap: 34px;
    text-transform: uppercase;
    font-size: 17px;
  }
  .services__lead { color: var(--text-dim); }
  .services__list { list-style: none; color: var(--text-light); }
  .services__list li { position: relative; padding-left: 26px; margin: 8px 0; }
  .services__list li::before {
    content: "";
    position: absolute;
    left: 0; top: 7px;
    width: 10px; height: 10px;
    border-radius: 50%;
    background: var(--green);
  }
</style>
</head>
<body>

<section class="card card--front" aria-label="Business card front">
  <div class="wordmark">Soft Belan</div>
  <div class="name-band"></div>
  <div class="holder">
    <div class="holder__name">Gerald Vanholt</div>
    <div class="holder__role">Director</div>
  </div>
  <div class="divider"></div>

  <div class="contact contact--left">
    <div class="contact__item">
      <svg class="contact__icon" width="26" height="20" viewBox="0 0 26 20" aria-hidden="true">
        <path d="M2 6 Q13 -1 24 6 L22 9 L18 8 L18 6 Q13 4 8 6 L8 8 L4 9 Z" fill="#cfcfcf"/>
        <rect x="5" y="10" width="16" height="9" rx="1.5" fill="#cfcfcf"/>
        <circle cx="13" cy="14.5" r="2.4" fill="#333"/>
      </svg>
      <div class="contact__text">+49 (0) 5820 / 417 309</div>
    </div>
    <div class="contact__item">
      <svg class="contact__icon" width="26" height="18" viewBox="0 0 26 18" aria-hidden="true">
        <rect x="1" y="1" width="24" height="16" fill="#cfcfcf"/>
        <path d="M1 1 L13 10 L25 1" fill="none" stroke="#333" stroke-width="1.5"/>
      </svg>
      <div class="contact__text contact__text--light">info@softbelan-studio.de</div>
    </div>
  </div>

  <div class="contact contact--right">
    <div class="contact__item">
      <svg class="contact__icon" width="34" height="34" viewBox="0 0 34 34" aria-hidden="true">
        <g fill="none" stroke="#cfcfcf" stroke-width="1.6">
          <circle cx="17" cy="17" r="15"/>
          <ellipse cx="17" cy="17" rx="7" ry="15"/>
          <line x1="17" y1="2" x2="17" y2="32"/>
          <line x1="2" y1="17" x2="32" y2="17"/>
          <path d="M5 9 H29 M5 25 H29"/>
        </g>
      </svg>
      <div class="contact__text contact__text--bold">www.softbelan-studio.de</div>
    </div>
  </div>
</section>

<section class="card card--back" aria-label="Business card back">
  <div class="wordmark">Soft Belan</div>
  <div class="services">
    <div class="services__lead">Software Development</div>
    <ul class="services__list">
      <li>App Development (iOS &amp; Android)</li>
      <li>Website Development</li>
    </ul>
  </div>
</section>

</body>
</html>
```